Brisbane IT support business needs our first business card

Hello we are a Brisbane based Information Technology company providing support and services to small and medium sized businesses. We provide a range of services and solutions.

The business name is Wattleridge Computer Services Group, or WCSG for short.

I am looking for a business card that looks professional (don't we all want that), but most importantly, it most utilize the colours in the logo attached.

Other business owners seeking our IT services, and also home users.

Business

• Please only use the blue/orange colours in logo attached

```html
<!DOCTYPE html>
<html lang="en">
<head>
<meta charset="utf-8">
<title>Wattleridge Computer Services Group – Business Card</title>
<link rel="stylesheet" href="https://fonts.googleapis.com/css2?family=Montserrat:wght@400;500;600;700;800&display=swap">
<style>
  :root {
    --navy: #1f4e6e;
    --navy-deep: #174462;
    --navy-soft: #2a5b7c;
    --orange: #f08a24;
    --orange-light: #f4a352;
    --white: #ffffff;
    --page: #ffffff;
  }
  * { box-sizing: border-box; margin: 0; padding: 0; }
  html, body { width: 1200px; height: 402px; overflow: hidden; background: var(--page); }
  body { position: relative; font-family: "Montserrat", Arial, sans-serif; }

  .card {
    position: absolute;
    top: 18px;
    height: 364px;
    overflow: hidden;
    box-shadow: 3px 4px 6px rgba(0,0,0,0.35);
  }
  .card-front { left: 18px; width: 572px; background: var(--white); }
  .card-back { left: 606px; width: 584px; background: var(--navy); }
  .card-art { position: absolute; inset: 0; }

  .brand { position: absolute; display: flex; align-items: center; }
  .brand-mark { border-radius: 50%; flex: none; }
  .brand-divider { flex: none; }
  .brand-name { font-weight: 800; line-height: 0.9; letter-spacing: 1px; }
  .brand-full { font-weight: 700; text-transform: uppercase; line-height: 1.05; }

  /* front */
  .card-front .brand { left: 34px; top: 63px; }
  .card-front .brand-mark { width: 104px; height: 104px; background: var(--navy); }
  .card-front .brand-divider { width: 2px; height: 74px; background: var(--orange); margin: 0 18px 0 20px; }
  .card-front .brand-name { color: var(--orange); font-size: 44px; }
  .card-front .brand-full { color: var(--navy); font-size: 10px; margin-top: 8px; }

  .person { position: absolute; left: 34px; top: 208px; color: var(--navy); font-weight: 700; }
  .person-name { font-size: 20px; padding-bottom: 4px; border-bottom: 3px solid var(--orange); display: inline-block; letter-spacing: 0.3px; }
  .person-role { font-size: 16px; margin-top: 14px; }

  .contact-list { position: absolute; left: 290px; top: 203px; width: 270px; list-style: none; }
  .contact-item { display: flex; align-items: center; height: 30px; margin-bottom: 13px; color: var(--white); font-size: 16px; font-weight: 400; white-space: nowrap; }
  .contact-icon { width: 30px; height: 30px; margin-right: 12px; flex: none; }

  /* back */
  .card-back .brand { left: 69px; top: 82px; }
  .card-back .brand-mark { width: 166px; height: 166px; background: var(--white); }
  .card-back .brand-divider { width: 2px; height: 108px; background: var(--white); margin: 0 26px 0 23px; }
  .card-back .brand-name { color: var(--white); font-size: 68px; }
  .card-back .brand-full { color: var(--white); font-size: 13.5px; margin-top: 10px; }
  .tagline { position: absolute; left: 0; right: 0; top: 262px; text-align: center; color: var(--white); font-weight: 700; font-size: 15.5px; line-height: 23px; text-transform: uppercase; letter-spacing: 0.5px; }
</style>
</head>
<body>

<section class="card card-front">
  <svg class="card-art" width="572" height="364" viewBox="0 0 572 364">
    <defs>
      <linearGradient id="city-front" x1="0" y1="0" x2="0" y2="1">
        <stop offset="0" stop-color="#2a5b7c"/>
        <stop offset="1" stop-color="#234f6f"/>
      </linearGradient>
    </defs>
    <rect x="0" y="0" width="572" height="32" fill="var(--orange)"/>
    <rect x="0" y="0" width="572" height="12" fill="var(--orange-light)" opacity="0.5"/>
    <path d="M222 332 C 255 205, 410 122, 572 120 L572 332 Z" fill="var(--navy)"/>
    <path d="M250 332 C 290 230, 420 150, 572 146 L572 332 Z" fill="url(#city-front)" role="img" aria-label="Faint city skyline silhouette"/>
    <path d="M222 332 C 255 205, 410 122, 572 120" fill="none" stroke="var(--orange)" stroke-width="4"/>
    <rect x="0" y="330" width="572" height="34" fill="var(--orange)"/>
    <polygon points="345,330 366,330 348,364 327,364" fill="var(--navy)"/>
  </svg>

  <div class="brand">
    <span class="brand-mark"></span>
    <span class="brand-divider"></span>
    <div>
      <div class="brand-name">WCSG</div>
      <div class="brand-full">Wattleridge Computer<br>Services Group</div>
    </div>
  </div>

  <div class="person">
    <div class="person-name">Kieran Dale</div>
    <div class="person-role">Director</div>
  </div>

  <ul class="contact-list">
    <li class="contact-item">
      <svg class="contact-icon" viewBox="0 0 30 30"><circle cx="15" cy="15" r="15" fill="var(--orange)"/><circle cx="15" cy="15" r="11" fill="none" stroke="#fff" stroke-width="1.5"/><path d="M11 9 l3 0 l1 4 l-2 1.5 a9 9 0 0 0 3.5 3.5 l1.5 -2 l4 1 l0 3 a2 2 0 0 1 -2 2 a13 13 0 0 1 -11 -11 a2 2 0 0 1 2 -2z" fill="#fff"/></svg>
      0412 367 914
    </li>
    <li class="contact-item">
      <svg class="contact-icon" viewBox="0 0 30 30"><circle cx="15" cy="15" r="15" fill="var(--orange)"/><rect x="7.5" y="9.5" width="15" height="11" rx="1" fill="#fff"/><path d="M7.5 10 L15 16 L22.5 10" fill="none" stroke="var(--orange)" stroke-width="1.4"/></svg>
      info@wattleridgecsg.com
    </li>
    <li class="contact-item">
      <svg class="contact-icon" viewBox="0 0 30 30"><circle cx="15" cy="15" r="15" fill="var(--orange)"/><g fill="none" stroke="#fff" stroke-width="1.5"><circle cx="15" cy="15" r="8"/><ellipse cx="15" cy="15" rx="3.5" ry="8"/><line x1="7" y1="15" x2="23" y2="15"/><line x1="8.5" y1="11" x2="21.5" y2="11"/><line x1="8.5" y1="19" x2="21.5" y2="19"/></g></svg>
      www.wattleridgecsg.com
    </li>
  </ul>
</section>

<section class="card card-back">
  <svg class="card-art" width="584" height="364" viewBox="0 0 584 364">
    <defs>
      <linearGradient id="city-back" x1="0" y1="0" x2="0" y2="1">
        <stop offset="0" stop-color="#1f4e6e"/>
        <stop offset="1" stop-color="#2a5b7c"/>
      </linearGradient>
    </defs>
    <rect x="0" y="170" width="584" height="164" fill="url(#city-back)" role="img" aria-label="Faint city skyline and bridge silhouette"/>
    <rect x="0" y="332" width="584" height="32" fill="var(--orange)"/>
    <polygon points="368,332 390,332 372,364 350,364" fill="var(--navy)"/>
  </svg>

  <div class="brand">
    <span class="brand-mark"></span>
    <span class="brand-divider"></span>
    <div>
      <div class="brand-name">WCSG</div>
      <div class="brand-full">Wattleridge Computer<br>Services Group</div>
    </div>
  </div>

  <p class="tagline">Brisbane’s leading innovator<br>of technology solutions</p>
</section>

</body>
</html>
```